rk ironcraft business card metallic look

revamp the existing design but want card to have a metalic look to it

Target Market(s)

construction industry

Industry/Entity Type

constrction

Contact Information for Business Card

front of card RK Ironcraft, phone 4165550193, email rk.ironcraftt@veltrano.com and instagram account; rk_ironcraft_

Font styles to use
Other font styles liked:
• masculine

Colors

Designer to choose only greyscale colors for use in the design.

Requirements
Must have
• back side RK Ironcraft then a list of everything : Siding, ACM Panels, Standing Seam,Soffit, Fascia, Gutters,Metal,Alu,inum, Viynyl, Metal Roofs and roof repairs
Nice to have
• I would like to keep the look of the existing card with the metal grids on the front
Should not have
• Need a design in two days

```html
<!DOCTYPE html>
<html lang="en">
<head>
<meta charset="utf-8">
<title>RK Ironcraft – Business Card</title>
<link href="https://fonts.googleapis.com/css2?family=Archivo:wght@400;700;800&display=swap" rel="stylesheet">
<style>
  :root{
    --stage:#000000;
    --card:#2b2b2b;
    --ink-light:#f2f2f2;
    --ink-dark:#111111;
    --steel-1:#f4f4f4;
    --steel-2:#b9bbbd;
    --steel-3:#8d8f91;
    --steel-4:#4a4a4a;
    --steel-5:#1c1c1c;
  }
  *{box-sizing:border-box;margin:0;padding:0}
  html,body{width:1200px;height:1200px;overflow:hidden;background:var(--stage)}
  .stage{position:relative;width:1200px;height:1200px;background:var(--stage);font-family:"Archivo",Arial,sans-serif}

  .card{position:absolute;left:276px;width:688px;height:400px;background:var(--card);overflow:hidden}
  .card--front{top:142px}
  .card--back{top:658px;height:402px}

  .brand-name{
    position:absolute;font-weight:800;color:var(--ink-light);
    text-transform:uppercase;letter-spacing:1px;line-height:1;white-space:nowrap;
  }
  .card--front .brand-name{left:70px;top:88px;font-size:44px}
  .card--back .brand-name{left:0;right:0;top:88px;font-size:46px;text-align:center}

  .contact-list{position:absolute;left:70px;top:176px;list-style:none}
  .contact-list li{display:flex;align-items:center;height:34px;color:var(--ink-light);font-size:20px;font-weight:400;letter-spacing:.2px}
  .contact-icon{width:25px;height:25px;margin-right:9px;flex:none}

  .chevron{position:absolute;left:0;top:0;width:688px;height:400px}

  .metal-band{
    position:absolute;left:0;top:202px;width:100%;height:26px;
    background:linear-gradient(90deg,#3a3a3a,#9a9a9a 15%,#2e2e2e 30%,#b5b5b5 48%,#333 62%,#a3a3a3 80%,#3c3c3c);
  }
  .steel-panel{
    position:absolute;left:0;top:228px;width:100%;height:174px;
    background:linear-gradient(90deg,#c9cacb 0%,#f3f3f3 18%,#a9abad 38%,#f0f0f0 58%,#b4b6b8 78%,#e6e6e6 100%);
  }
  .service-list{position:absolute;top:22px;list-style:none}
  .service-list--a{left:84px}
  .service-list--b{left:295px}
  .service-list--c{left:464px}
  .service-list li{display:flex;align-items:center;height:31.5px;font-size:19px;font-weight:700;color:var(--ink-dark)}
  .service-list li::before{content:"";width:12px;height:12px;border:2px solid var(--ink-dark);margin-right:9px;flex:none}
</style>
</head>
<body>
<main class="stage">

  <section class="card card--front" aria-label="Business card front">
    <svg class="chevron" viewBox="0 0 688 400" aria-hidden="false">
      <defs>
        <linearGradient id="frameSteel" x1="0" y1="0" x2="1" y2="1">
          <stop offset="0" stop-color="#f2f2f2"/>
          <stop offset=".45" stop-color="#7d7f81"/>
          <stop offset=".7" stop-color="#e4e4e4"/>
          <stop offset="1" stop-color="#6a6a6a"/>
        </linearGradient>
        <linearGradient id="grilleTone" x1="0" y1="0" x2="1" y2="0">
          <stop offset="0" stop-color="#3a3a3a"/>
          <stop offset=".3" stop-color="#8e8e8e"/>
          <stop offset=".55" stop-color="#444"/>
          <stop offset=".8" stop-color="#a6a6a6"/>
          <stop offset="1" stop-color="#3d3d3d"/>
        </linearGradient>
      </defs>
      <polygon points="426,200 688,0 688,400" fill="url(#frameSteel)"/>
      <polygon points="440,200 688,12 688,388" fill="var(--card)"/>
      <polygon points="448,200 688,20 688,380" fill="url(#grilleTone)" role="img" aria-label="Brushed metal grille panel"/>
    </svg>

    <p class="brand-name">RK Ironcraft</p>

    <ul class="contact-list">
      <li>
        <svg class="contact-icon" viewBox="0 0 24 24" aria-hidden="true">
          <circle cx="12" cy="12" r="10.5" fill="none" stroke="#f2f2f2" stroke-width="1.6"/>
          <path d="M8.2 6.5c.5-.4 1.1-.3 1.4.2l1.1 1.8c.3.5.2 1-.2 1.3l-.8.6c.6 1.4 1.6 2.5 3 3.1l.6-.8c.3-.4.9-.5 1.3-.2l1.8 1.1c.5.3.6.9.2 1.4l-.8.9c-.6.6-1.5.8-2.3.5-3-1.1-5.2-3.4-6.3-6.3-.3-.8-.1-1.7.5-2.3z" fill="#f2f2f2"/>
        </svg>
        4165550193
      </li>
      <li>
        <svg class="contact-icon" viewBox="0 0 24 24" aria-hidden="true">
          <circle cx="12" cy="12" r="10.5" fill="none" stroke="#f2f2f2" stroke-width="1.6"/>
          <rect x="6.5" y="8" width="11" height="8" fill="none" stroke="#f2f2f2" stroke-width="1.4"/>
          <path d="M6.5 8l5.5 4.5L17.5 8M6.5 16l4-3.5M17.5 16l-4-3.5" fill="none" stroke="#f2f2f2" stroke-width="1.2"/>
        </svg>
        rk.ironcraftt@veltrano.com
      </li>
      <li>
        <svg class="contact-icon" viewBox="0 0 24 24" aria-hidden="true">
          <circle cx="12" cy="12" r="10.5" fill="none" stroke="#f2f2f2" stroke-width="1.6"/>
        </svg>
        rk_ironcraft_
      </li>
    </ul>
  </section>

  <section class="card card--back" aria-label="Business card back">
    <p class="brand-name">RK Ironcraft</p>
    <div class="metal-band" role="img" aria-label="Brushed metal grille strip"></div>
    <div class="steel-panel">
      <ul class="service-list service-list--a">
        <li>Siding</li>
        <li>ACM Panels</li>
        <li>Standing Seam</li>
        <li>Soffit</li>
      </ul>
      <ul class="service-list service-list--b">
        <li>Fascia</li>
        <li>Gutters</li>
        <li>Metal</li>
        <li>Aluminium</li>
      </ul>
      <ul class="service-list service-list--c">
        <li>Viynyl</li>
        <li>Metal Roofs</li>
        <li>Roof Repairs</li>
      </ul>
    </div>
  </section>

</main>
</body>
</html>
```